Asian Pakistani: Wedding Invitation

Design a pakistani asian wedding invitation.
Islamic theme, with arabic text:

Text to be used:

Start with: bismillah and dua for marriage. (The Holy Quran chapter 25 verse 75 with arabic text and english translation below)

Mrs. Rubina Sohail wife of (late) Mr. Sohail Imran Qureshi
Cordially requests your company to grace the joyous occasion of the wedding of their beloved daughter
Mehreen Qureshi
Daughter of ( late) Mr Sohail Imran qureshi
with
Bilal Siddiqui
Son of Mr. Junaid Siddiqui & Mrs Shazia Siddiqui

Insha’Allah on Thursday 29th August 2019 at Velvet Orchard
12 Marlow Crescent, Croydon
CR7 2LP
Baraat Arrival 6:30

RSVP
Usman Qureshi 07700 900412
Tariq Mehmood 07700 900583
Faisal Butt 07700 900735

Target Market(s)

Muslims

Font styles to use
Script

Colors

Designer to choose colors to be used in the design.

Requirements
Must have
• stylish calligraphy Arabic lettering of the dua requested above
• Size:
• Long 4" x 9.5"
Nice to have
• ottoman empire: Art theme

```html
<!DOCTYPE html>
<html lang="en">
<head>
<meta charset="utf-8">
<title>Wedding Invitation – Mehreen &amp; Bilal</title>
<link rel="stylesheet" href="https://fonts.googleapis.com/css2?family=Amiri:wght@400;700&family=Aref+Ruqaa:wght@400;700&family=Great+Vibes&family=Libre+Baskerville:ital,wght@0,400;0,700;1,400&display=swap">
<style>
  :root {
    --backdrop: #3b3b3d;
    --crimson: #8c1b2c;
    --crimson-deep: #6d0f1f;
    --crimson-light: #a32a3b;
    --panel: rgba(255, 235, 220, 0.06);
    --cream: #f6e6cf;
    --gold: #e7c89a;
    --white: #fff8ef;
  }
  * { margin: 0; padding: 0; box-sizing: border-box; }
  html, body { width: 1200px; height: 2356px; overflow: hidden; background: var(--backdrop); }
  .canvas { position: relative; width: 1200px; height: 2356px; }
  .card {
    position: absolute; left: 56px; top: 32px; width: 1088px; height: 2288px;
    background: radial-gradient(ellipse at 50% 14%, var(--crimson-light) 0%, var(--crimson) 40%, var(--crimson-deep) 100%);
    box-shadow: 0 10px 40px rgba(0,0,0,.45);
    color: var(--white); text-align: center;
    font-family: "Libre Baskerville", Georgia, serif;
  }
  .card-pattern {
    position: absolute; left: 0; top: 0; width: 100%; height: 720px;
    background: radial-gradient(circle at 50% 45%, rgba(255,220,200,.12) 0%, rgba(255,220,200,0) 62%);
  }
  .medallion {
    position: absolute; left: 384px; top: 208px; width: 320px; height: 320px; border-radius: 50%;
    background: radial-gradient(circle, #f3ddbf 0%, #d9b58a 35%, #b98a5e 62%, rgba(185,138,94,0.15) 100%);
  }
  .inner-panel {
    position: absolute; left: 64px; top: 808px; width: 960px; height: 1320px;
    background: var(--panel);
  }
  .line { position: absolute; left: 0; width: 100%; white-space: nowrap; }
  .bismillah { top: 571px; line-height: 90px; font-family: "Aref Ruqaa", "Amiri", serif; font-size: 64px; color: var(--cream); direction: rtl; }
  .bismillah-en { top: 737px; line-height: 30px; font-size: 22px; }
  .dua { top: 848px; font-family: "Aref Ruqaa", "Amiri", serif; font-size: 54px; line-height: 96px; color: var(--cream); direction: rtl; }
  .ayah-mark { top: 1031px; line-height: 50px; font-family: "Amiri", serif; font-size: 40px; color: var(--cream); }
  .translation { top: 1112px; font-size: 21px; line-height: 32px; }
  .divider { top: 1245px; }
  .host { top: 1305px; line-height: 30px; font-size: 20px; font-weight: 700; }
  .request { top: 1338px; font-size: 21px; line-height: 36px; }
  .couple-name { font-family: "Great Vibes", cursive; font-size: 70px; line-height: 80px; color: var(--cream); }
  .bride { top: 1432px; }
  .parentage { font-size: 25px; line-height: 36px; }
  .bride-parent { top: 1530px; }
  .conjunction { top: 1586px; font-size: 25px; line-height: 36px; }
  .groom { top: 1624px; }
  .groom-parent { top: 1700px; }
  .event-box {
    position: absolute; left: 232px; top: 1788px; width: 624px; height: 220px;
    border: 2px solid var(--gold);
  }
  .event-banner {
    position: absolute; left: 102px; top: -26px; width: 420px; height: 52px;
    background: var(--cream); color: var(--crimson);
    font-family: "Great Vibes", cursive; font-size: 38px; line-height: 54px; white-space: nowrap;
  }
  .event-details { position: absolute; left: 0; top: 66px; width: 100%; font-size: 22px; line-height: 48px; }
  .event-details strong { font-weight: 700; }
  .rsvp-rule { position: absolute; left: 104px; top: 2030px; width: 880px; height: 2px; background: var(--gold); opacity: .7; }
  .rsvp-title { top: 2045px; line-height: 30px; font-size: 24px; font-weight: 700; letter-spacing: 6px; }
  .contacts { position: absolute; left: 64px; top: 2098px; width: 960px; display: flex; justify-content: space-around; }
  .contact { font-size: 20px; line-height: 36px; font-weight: 700; }
</style>
</head>
<body>
<div class="canvas">
  <article class="card">
    <div class="card-pattern" role="img" aria-label="Faint Ottoman floral pattern behind the header"></div>
    <div class="medallion" role="img" aria-label="Ornate gold Islamic mandala medallion"></div>
    <div class="inner-panel"></div>

    <p class="line bismillah">بِسْمِ ٱللَّٰهِ ٱلرَّحْمَٰنِ ٱلرَّحِيمِ</p>
    <p class="line bismillah-en">In the name of Allah, the most Gracious, most Merciful</p>

    <p class="line dua">رَبَّنَا هَبْ لَنَا مِنْ أَزْوَاجِنَا وَذُرِّيَّاتِنَا<br>قُرَّةَ أَعْيُنٍ وَاجْعَلْنَا لِلْمُتَّقِينَ إِمَامًا</p>
    <p class="line ayah-mark">۝٧٥</p>
    <p class="line translation">Our Lord, Grant us of our Wives and Children the delight<br>of our Eyes, and make us a Model of the righteous<br>(Sura Al-Furqan:75)</p>

    <svg class="line divider" width="1088" height="30" viewBox="0 0 1088 30">
      <g fill="none" stroke="#f6e6cf" stroke-width="2">
        <line x1="356" y1="15" x2="516" y2="15"/>
        <line x1="572" y1="15" x2="732" y2="15"/>
        <path d="M516 15 q14 -12 28 0 q14 12 28 0"/>
        <path d="M516 15 q14 12 28 0 q14 -12 28 0"/>
      </g>
      <circle cx="544" cy="15" r="4" fill="#f6e6cf"/>
      <circle cx="352" cy="15" r="3" fill="#f6e6cf"/>
      <circle cx="736" cy="15" r="3" fill="#f6e6cf"/>
    </svg>

    <p class="line host">Mrs. Rubina Sohail wife of (late) Mr. Sohail Imran Qureshi</p>
    <p class="line request">Cordially requests your company to grace the joyous<br>occasion of the wedding of their beloved daughter</p>

    <p class="line couple-name bride">Mehreen Qureshi</p>
    <p class="line parentage bride-parent">Daughter of ( late) Mr Sohail Imran qureshi</p>
    <p class="line conjunction">with</p>
    <p class="line couple-name groom">Bilal Siddiqui</p>
    <p class="line parentage groom-parent">Son of Mr. Junaid Siddiqui &amp; Mrs Shazia Siddiqui</p>

    <section class="event-box">
      <div class="event-banner">Insha’Allah on Thursday</div>
      <div class="event-details">
        <p><strong>29th August 2019</strong> at Velvet Orchard</p>
        <p>12 Marlow Crescent, Croydon, CR7 2LP</p>
        <p><strong>Baraat Arrival 6:30</strong></p>
      </div>
    </section>

    <div class="rsvp-rule"></div>
    <p class="line rsvp-title">RSVP</p>
    <div class="contacts">
      <p class="contact">Usman Qureshi<br>07700 900412</p>
      <p class="contact">Tariq Mehmood<br>07700 900583</p>
      <p class="contact">Faisal Butt<br>07700 900735</p>
    </div>
  </article>
</div>
</body>
</html>
```